KRV Construction Management -Business card design request- Lioness black and white shema ONLY - No

It is a woman on construction company I would like the schema to be in black-and-white with the lioness and possibly a lion anulinus as me and my husband both kind of running I would like to see designs for both. Original art would be preferred but like I said I'm going to attach some pictures that I really like and also if you could check my website out that would be great.Please get very creative this is a very important company I will be combining quality construction services with quality construction company and community affiliates such as Halvick construction exedra I really need to show dominates all I'm really wanting is the black-and-white montre and the lioness image on the right side as you will see in some of the thumbnails from what I have had in the past it is OK but I can't connect with anything. These are the last of my advertising dollars I ask that you really please put some time and help me take my company it to the next century. This is going to be a global thing it will be very serious. I'm not trying to be arrogant I'm just trying to tell the truth I ask that you give me something of quality that something that I can put on folders billboards pains walking to places and that it's not that I'm a woman own business but I deftly want there to be A-line as and please play around with the image of the lion and lioness as my husband is a lot of the construction side and I have a decided if Im going to advertise that are notJmsconstructionmanagement.comJovanna Schlossenberg C.E.O.KRV Construction Management Marisela@jmsconstructionmanagement.com81.316.0990

Target Market(s)

Construction or management style. Understand theme ports of marketing and that this logo will be displayed on billboards D cows apps all across the country

Industry/Entity Type

Construction Company

Contact Information for Business Card

Marisela Vandertook
C.E.O.

Marisela@krvconstructionmanagement.example

Www.krvconstructionmanagement.example

729.584.1437

If you can I would like my slogan on their connecting qualify construction services with qualified construction companies and community affiliates

Font styles to use
Sans Serif

Colors
ffffff

Requirements
Must have
• Black-and-white schema lioness on the back side I will list my services will get to that but for now I wanna get the logo design I very open to where you maneuver the contact information
• Marisela Vandertook
• C.E.O.
• Marisela@krvconstructionmanagement.example
• Www.krvconstructionmanagement.example
• 729.584.1437
• If you can I would like my slogan on their connecting qualified construction services with qualified construction companies and community affiliates
Nice to have
• Everything I mentioned above.
• I have added a few pictures with a lion and Linus and know this may seem crazy but I do not like that they are facing to the left I would rather the lion and lioness looked to the right and face forward. Also all the images need to be in black-and-white have provided some color want but I'd like them change to sepia .
Should not have
• I do not want it to look like a cartoon I need this to be of the utmost professionalism

```html
<!DOCTYPE html>
<html lang="en">
<head>
<meta charset="utf-8">
<title>KRV Construction Management – Business Card</title>
<link href="https://fonts.googleapis.com/css2?family=Roboto:wght@500;700&family=Montserrat:wght@500;600&display=swap" rel="stylesheet">
<style>
  :root {
    --canvas: #f4f4f4;
    --card-dark: #1e1e1e;
    --card-light: #e6e6e6;
    --ink: #111111;
    --ink-soft: #2a2a2a;
    --rule: #bdbdbd;
    --back-text: #c9c9c9;
    --mark-light: #bfbfbf;
  }
  * { margin: 0; padding: 0; box-sizing: border-box; }
  html, body {
    width: 1200px; height: 862px; overflow: hidden;
    background: var(--canvas);
    font-family: "Roboto", Arial, sans-serif;
  }
  .sheet {
    position: relative; width: 1200px; height: 862px;
  }
  .card {
    position: absolute; top: 245px;
    width: 560px; height: 373px;
    border-radius: 22px; overflow: hidden;
  }

  /* Back side */
  .card--back { left: 20px; background: var(--card-dark); }
  .card__photo {
    position: absolute; inset: 0;
    background:
      radial-gradient(ellipse 45% 55% at 30% 55%, rgba(70,70,70,.55), transparent 70%),
      radial-gradient(ellipse 40% 50% at 58% 50%, rgba(80,80,80,.5), transparent 70%),
      linear-gradient(180deg, #262626 0%, #1c1c1c 60%, #2a2a2a 100%);
  }
  .card__url {
    position: absolute; top: 38px; right: 57px;
    font-weight: 700; font-size: 14px; letter-spacing: 1.3px;
    color: var(--back-text);
  }
  .wordmark { position: absolute; display: flex; align-items: center; gap: 10px; }
  .wordmark__dot { width: 30px; height: 30px; border-radius: 50%; }
  .wordmark__text { display: flex; flex-direction: column; line-height: 1; font-family: "Montserrat", Arial, sans-serif; font-weight: 600; }
  .wordmark__name { letter-spacing: 3px; }
  .wordmark__sub { letter-spacing: 1.3px; margin-top: 4px; }

  .card--back .wordmark { left: 328px; top: 205px; color: var(--mark-light); }
  .card--back .wordmark__dot { background: var(--mark-light); }
  .card--back .wordmark__name { font-size: 40px; }
  .card--back .wordmark__sub { font-size: 7px; }

  /* Front side */
  .card--front { left: 620px; background: var(--card-light); color: var(--ink); }
  .card__tab {
    position: absolute; left: 0; top: 79px;
    width: 15px; height: 189px;
    background: var(--ink); border-radius: 0 10px 10px 0;
  }
  .card--front .wordmark { left: 50%; top: 50px; transform: translateX(-50%); color: var(--ink); }
  .card--front .wordmark__dot { background: var(--ink); width: 26px; height: 26px; }
  .card--front .wordmark__name { font-size: 32px; }
  .card--front .wordmark__sub { font-size: 6px; }

  .person {
    position: absolute; left: 64px; top: 128px;
    font-weight: 700; font-size: 25px; letter-spacing: 2.4px;
    color: var(--ink-soft);
  }
  .rule {
    position: absolute; left: 64px; top: 182px;
    width: 428px; height: 1px; background: var(--rule);
  }
  .contacts { position: absolute; left: 64px; top: 194px; list-style: none; }
  .contact {
    display: flex; align-items: center; gap: 9px;
    height: 28px; margin-bottom: 13.5px;
    font-weight: 700; font-size: 15px; letter-spacing: 1.4px;
    color: var(--ink-soft);
  }
  .contact__icon { width: 28px; height: 28px; flex: none; }
</style>
</head>
<body>
<main class="sheet">

  <section class="card card--back" aria-label="Card back">
    <div class="card__photo" role="img" aria-label="Black and white photograph of a lion and a lioness resting side by side"></div>
    <p class="card__url">krvconstructionmanagement.com</p>
    <div class="wordmark">
      <span class="wordmark__dot"></span>
      <span class="wordmark__text">
        <span class="wordmark__name">KRV</span>
        <span class="wordmark__sub">CONSTRUCTION MANAGEMENT</span>
      </span>
    </div>
  </section>

  <section class="card card--front" aria-label="Card front">
    <span class="card__tab"></span>
    <div class="wordmark">
      <span class="wordmark__dot"></span>
      <span class="wordmark__text">
        <span class="wordmark__name">KRV</span>
        <span class="wordmark__sub">CONSTRUCTION MANAGEMENT</span>
      </span>
    </div>
    <h1 class="person">Marisela Vandertook(C.E.O.)</h1>
    <span class="rule"></span>
    <ul class="contacts">
      <li class="contact">
        <svg class="contact__icon" viewBox="0 0 28 28" aria-hidden="true">
          <circle cx="14" cy="14" r="14" fill="#111"/>
          <rect x="7.5" y="9.5" width="13" height="9" fill="#fff"/>
          <path d="M7.5 9.5 L14 15 L20.5 9.5" fill="none" stroke="#111" stroke-width="1.3"/>
        </svg>
        Marisela@krvconstructionmanagement.example
      </li>
      <li class="contact">
        <svg class="contact__icon" viewBox="0 0 28 28" aria-hidden="true">
          <circle cx="14" cy="14" r="14" fill="#111"/>
          <path d="M10 8 L12.5 8 L13.3 11 L11.8 12.2 C12.6 14 14 15.4 15.8 16.2 L17 14.7 L20 15.5 L20 18 C20 19 19 20 18 20 C12.5 19.6 8.4 15.5 8 10 C8 9 9 8 10 8 Z" fill="#fff"/>
        </svg>
        www.krvconstructionmanagement.example
      </li>
      <li class="contact">
        <svg class="contact__icon" viewBox="0 0 28 28" aria-hidden="true">
          <circle cx="14" cy="14" r="14" fill="#111"/>
          <g fill="none" stroke="#fff" stroke-width="1.3">
            <circle cx="14" cy="14" r="7"/>
            <ellipse cx="14" cy="14" rx="3" ry="7"/>
            <line x1="7" y1="14" x2="21" y2="14"/>
            <line x1="8.2" y1="10.5" x2="19.8" y2="10.5"/>
            <line x1="8.2" y1="17.5" x2="19.8" y2="17.5"/>
          </g>
        </svg>
        729.584.1437
      </li>
    </ul>
  </section>

</main>
</body>
</html>
```